Business card design needed

I am a business consultant but I call myself an "organizational leadership consultant." My clients hire me to do organizational development work in the areas of leadership development, strategic planning, shared visioning, governance (bylaws, policy, board development), collaborative capacity building, and organizational communications. I work in numerous sectors (public, private, not-for-profit and governmental) but most of my clients are in not-for-profit (but not human service - think national advocacy organizations, student governments, regulatory colleges, and professional (accreditation) bodies).

I want my cards to convey the concepts of being reliable and smart (of course) but also vibrant and signifying new beginnings/possibilities.

I am uploading a copy of a logo I have used for some time (adapted from QX logo free website). I like the hues of the primary colours used, its symmetrical, and that it has movement. I am open to a new logo (but not essential) with these same qualities: I really like fractals BTW.

I think one of the most beautiful creatures on earth is the harlequin duck, but have not been able to figure out how to incorporate that into my brand. Mostly what I love is the colours and how they appear on the duck. I am sharing that just as an idea in case your creative energy is leaning toward creating a new design rather than working with my logo.

If I had the right business card to start with, I might consider re-branding and working that into my digital and print materials. I realize this is against the use of RGBY in my current logo.
Updates

Hi - I forgot to mention to please use the PVRA Certified patch/logo as a just a small feature of the card - it is not my main logo. Also, I like fonts that are clean.  Thanks!

Target Market(s)

Higher level business professionals

Industry/Entity Type

Business Consultant

Contact Information for Business Card

Corla Whitfield, MA, BSc, PVRA(pls insert trademark symbol)
Organizational Leadership Consultant
250-487-6019
corla@cwhitfieldadvisory.example
www.cwhitfieldadvisory.example
Alderwood Cove, BC

Logo Text

Leadership Consulting for a New Future

Logo styles of interest
Emblem Logo
Abstract Logo
Requirements
Must have
• Must have:
1. Name of my business (Corla Whitfield Consulting) and contact info per above
2. My logo (or your new idea for a logo) with a my tagline somewhere (tagline can be on back. Tagline is "Leadership Consulting for a New Future)
3. PVRA certified logo (attachment #3)
3. Chirpora logo with my acct name (@corlawhitfield), and
4. Workvine logo
Should not have
• I don't like the "solid" primary colours as in those found on brikko or in a pebblies box - transparency in those colours is acceptable.

Do not include images of people shaking hands or other corny 'business' imagery.;-)

```html
<!DOCTYPE html>
<html lang="en">
<head>
<meta charset="utf-8">
<title>Corla Whitfield Consulting – Business Card</title>
<link rel="stylesheet" href="https://fonts.googleapis.com/css2?family=Bebas+Neue&family=Arimo:wght@400&display=swap">
<style>
  :root {
    --brand-red: #b83427;
    --brand-gold: #e2aa27;
    --ink: #111111;
    --paper: #ffffff;
    --page: #ffffff;
  }
  html, body {
    margin: 0;
    padding: 0;
    width: 1200px;
    height: 1200px;
    overflow: hidden;
    background: var(--page);
  }
  .canvas {
    position: relative;
    width: 1200px;
    height: 1200px;
  }

  /* Front of card */
  .card-front {
    position: absolute;
    left: 137px;
    top: 78px;
    width: 888px;
    height: 547px;
    background: var(--paper);
    overflow: hidden;
  }
  .front-decoration {
    position: absolute;
    left: 0;
    top: 0;
    width: 308px;
    height: 491px;
    background: radial-gradient(ellipse 90% 70% at 0% 50%, rgba(184,52,39,0.55) 0%, rgba(184,52,39,0.25) 55%, rgba(184,52,39,0) 100%);
  }
  .identity {
    position: absolute;
    right: 55px;
    top: 240px;
    text-align: right;
  }
  .identity-name-line {
    display: flex;
    align-items: flex-end;
    justify-content: flex-end;
    gap: 0;
    line-height: 1;
  }
  .person-name {
    font-family: "Bebas Neue", sans-serif;
    font-size: 40px;
    color: var(--ink);
  }
  .credentials {
    font-family: "Arimo", sans-serif;
    font-size: 23px;
    color: var(--ink);
    margin-left: 7px;
    position: relative;
    top: -4px;
  }
  .credentials sup {
    font-size: 10px;
  }
  .cert-badge {
    width: 30px;
    height: 30px;
    margin-left: 6px;
    border-radius: 50%;
    background: var(--brand-gold);
    border: 3px solid var(--brand-red);
    box-sizing: border-box;
    position: relative;
    top: -12px;
  }
  .job-title {
    font-family: "Arimo", sans-serif;
    font-size: 23px;
    color: var(--ink);
    margin-top: 4px;
  }
  .contact {
    position: absolute;
    right: 55px;
    top: 383px;
    text-align: right;
    font-family: "Arimo", sans-serif;
    font-style: normal;
    font-size: 23px;
    line-height: 30px;
    color: var(--ink);
  }
  .footer-band {
    position: absolute;
    left: 0;
    bottom: 0;
    width: 100%;
    height: 56px;
    background: linear-gradient(to right, var(--brand-gold) 0%, var(--brand-gold) 69.3%, var(--brand-red) 69.3%, var(--brand-red) 100%);
  }
  .website {
    position: absolute;
    left: 45px;
    top: 9px;
    font-family: "Bebas Neue", sans-serif;
    font-size: 30px;
    line-height: 1.2;
    color: var(--paper);
  }
  .band-mark {
    position: absolute;
    left: 594px;
    top: 9px;
    width: 38px;
    height: 38px;
    border-radius: 50%;
    background: var(--paper);
  }

  /* Back of card */
  .card-back {
    position: absolute;
    left: 249px;
    top: 684px;
    width: 664px;
    height: 410px;
    background: var(--brand-gold);
  }
  .brand-dot {
    position: absolute;
    left: 206px;
    top: 36px;
    width: 252px;
    height: 252px;
    border-radius: 50%;
    background: var(--paper);
  }
  .brand-name {
    position: absolute;
    left: 0;
    width: 100%;
    top: 301px;
    text-align: center;
    font-family: "Bebas Neue", sans-serif;
    font-size: 49px;
    line-height: 1;
    color: var(--paper);
    letter-spacing: -2.2px;
  }
  .tagline {
    position: absolute;
    left: 0;
    width: 100%;
    top: 348px;
    text-align: center;
    font-family: "Arimo", sans-serif;
    font-size: 20px;
    line-height: 24px;
    color: var(--paper);
  }
</style>
</head>
<body>
<div class="canvas">

  <section class="card-front">
    <div class="front-decoration" role="img" aria-label="Decorative brand pattern in red"></div>

    <div class="identity">
      <div class="identity-name-line">
        <span class="person-name">Corla Whitfield,</span>
        <span class="credentials">MA, BSc, PVRA<sup>™</sup></span>
        <span class="cert-badge" role="img" aria-label="Certification badge"></span>
      </div>
      <div class="job-title">Organizational Leadership Consultant</div>
    </div>

    <address class="contact">
      <div>250-487-6019</div>
      <div>corla@cwhitfieldadvisory.example</div>
      <div>Alderwood Cove, BC</div>
    </address>

    <div class="footer-band">
      <span class="website">www.cwhitfieldadvisory.example</span>
      <span class="band-mark"></span>
    </div>
  </section>

  <section class="card-back">
    <span class="brand-dot" role="img" aria-label="Brand emblem"></span>
    <div class="brand-name">Corla Whitfield Consulting</div>
    <div class="tagline">Leadership Consulting for a New Future</div>
  </section>

</div>
</body>
</html>
```